LoomTrellis business card & letterhead
LoomTrellis letterhead and envelopes
I want to thank everyone for your great artwork. I really appreciate all of the inputs. Thank you again.
Pls check private message
Thanks
Paloma pixel
Nice drafts. Thank you all. Keep them coming. Please do not place a bar in the middle of the card.
Again: the title after the name is Ed.S.
So: Howard Winslow Ed.S.
I like the swirl (cycle) better than the straight lines.
Just keep it to single sided please.
Ok, I forgot to put my degree on the guide. It should be: Howard Winslow Ed.S.

```html
<!DOCTYPE html>
<html lang="en">
<head>
<meta charset="utf-8">
<title>LoomTrellis Stationery</title>
<link href="https://fonts.googleapis.com/css2?family=Open+Sans:wght@400;600;800&display=swap" rel="stylesheet">
<style>
:root{
  --bg:#ece5da;
  --paper:#ffffff;
  --ink:#1d2430;
  --muted:#7b8390;
  --blue:#1f4f8e;
  --blue-deep:#12345f;
  --green:#79bd2b;
  --black:#15171b;
  --faint:#eef1f4;
  --line:#b9c0c8;
}
*{box-sizing:border-box;margin:0;padding:0}
html,body{width:1200px;height:629px;overflow:hidden;background:var(--bg);font-family:"Open Sans",Arial,sans-serif;color:var(--ink)}
.canvas{position:relative;width:1200px;height:629px}
.item{position:absolute;background:var(--paper);box-shadow:0 2px 6px rgba(0,0,0,.25);overflow:hidden}
.label{position:absolute;font-size:7px;font-weight:600;color:var(--ink);text-align:center;white-space:nowrap}
.wave{position:absolute;left:0;bottom:0;width:100%}
.brand{display:flex;align-items:center;gap:4px;font-weight:800;color:var(--blue);white-space:nowrap}
.brand .dot{border-radius:50%;background:var(--green);flex:none}
.dark .brand{color:#fff}
.card{width:156px;height:91px}
.card.dark{background:var(--black)}
.card .brand{position:absolute;font-size:10px}
.card .brand .dot{width:12px;height:12px}
.card .info{position:absolute;right:8px;top:8px;font-size:4.5px;line-height:1.5;text-align:right;color:var(--ink)}
.card.dark .info{color:#dfe3e8}
.card .info strong{font-size:6px;display:block}
.sheet{width:324px;height:408px}
.sheet .brand{position:absolute;left:20px;top:16px;font-size:14px}
.sheet .brand .dot{width:18px;height:18px}
.emblem{position:absolute;border-radius:50%;background:radial-gradient(circle,var(--faint) 0 55%,#f6f7f9 56% 100%)}
.sheet .emblem{left:92px;top:130px;width:140px;height:140px}
.sheet .wave{height:70px}
.footer{position:absolute;right:16px;bottom:10px;font-size:4.5px;line-height:1.6;color:#fff;text-align:right}
.fax-title{position:absolute;right:20px;top:52px;font-size:8px;font-weight:800;color:var(--blue)}
.fax-table{position:absolute;left:20px;top:66px;width:284px;border-collapse:collapse;font-size:5px}
.fax-table td{border:.6px solid var(--line);height:13px;padding:0 3px}
.fax-table td.key{width:26px;color:var(--muted)}
.checks{position:absolute;left:20px;top:128px;display:flex;gap:14px;font-size:5px;color:var(--muted)}
.checks span::before{content:"";display:inline-block;width:5px;height:5px;border:.6px solid var(--line);margin-right:3px;vertical-align:middle}
.envelope-front{width:444px;height:182px}
.envelope-front .brand{position:absolute;left:18px;top:14px;font-size:13px}
.envelope-front .brand .dot{width:16px;height:16px}
.return{position:absolute;left:18px;top:36px;font-size:4.5px;color:var(--muted)}
.envelope-front .emblem{left:176px;top:26px;width:92px;height:92px}
.envelope-front .wave{height:44px}
.envelope-back{width:444px;height:100px}
.envelope-back svg.flap{position:absolute;left:0;top:0;width:100%;height:100%}
.seal{position:absolute;left:212px;top:42px;width:20px;height:20px;border-radius:50%;background:var(--green)}
.seal-text{position:absolute;left:0;width:100%;top:66px;font-size:4.5px;text-align:center;color:#fff}
</style>
</head>
<body>
<main class="canvas">
<svg width="0" height="0" style="position:absolute">
  <defs>
    <linearGradient id="blueband" x1="0" y1="0" x2="1" y2="0">
      <stop offset="0" stop-color="#12345f"/><stop offset="1" stop-color="#2a63a8"/>
    </linearGradient>
    <symbol id="swoosh" viewBox="0 0 100 30" preserveAspectRatio="none">
      <path d="M0 14 C30 4 60 26 100 6 L100 30 L0 30Z" fill="url(#blueband)"/>
      <path d="M0 12 C30 2 60 24 100 4" fill="none" stroke="#79bd2b" stroke-width="2"/>
    </symbol>
  </defs>
</svg>

<!-- business cards -->
<div class="label" style="left:91px;top:26px;width:156px">Business Card (Front)</div>
<section class="item card dark" style="left:91px;top:40px">
  <div class="brand" style="left:14px;top:30px"><span class="dot"></span>LoomTrellis</div>
  <svg class="wave" style="height:28px"><use href="#swoosh" width="100%" height="100%"/></svg>
</section>
<div class="label" style="left:252px;top:26px;width:156px">Business Card (Back)</div>
<section class="item card dark" style="left:252px;top:40px">
  <div class="info"><strong>Howard Winslow Ed.S.</strong>Director<br>555-0142<br>hello@loomtrellis.com</div>
  <div class="brand" style="left:10px;top:44px;font-size:8px"><span class="dot" style="width:10px;height:10px"></span>LoomTrellis</div>
  <svg class="wave" style="height:24px"><use href="#swoosh" width="100%" height="100%"/></svg>
</section>
<div class="label" style="left:413px;top:26px;width:156px">Business Card (Front)</div>
<section class="item card" style="left:413px;top:40px">
  <div class="info"><strong>Howard Winslow Ed.S.</strong>Director<br>555-0142<br>hello@loomtrellis.com</div>
  <div class="brand" style="left:10px;top:40px;font-size:8px"><span class="dot" style="width:10px;height:10px"></span>LoomTrellis</div>
  <svg class="wave" style="height:26px"><use href="#swoosh" width="100%" height="100%"/></svg>
</section>
<div class="label" style="left:571px;top:26px;width:156px">Business Card (Back)</div>
<section class="item card" style="left:571px;top:40px">
  <div class="brand" style="left:14px;top:28px"><span class="dot"></span>LoomTrellis</div>
  <div class="info" style="top:46px">12 Birch Lane<br>Dover, DE 19901</div>
  <svg class="wave" style="height:26px"><use href="#swoosh" width="100%" height="100%"/></svg>
</section>

<!-- fax cover -->
<div class="label" style="left:24px;top:192px;width:324px">Fax Cover</div>
<section class="item sheet" style="left:24px;top:204px">
  <div class="brand"><span class="dot"></span>LoomTrellis</div>
  <div class="fax-title">FAX</div>
  <table class="fax-table">
    <tr><td class="key">To:</td><td></td><td class="key">From:</td><td></td></tr>
    <tr><td class="key">Fax:</td><td></td><td class="key">Pages:</td><td></td></tr>
    <tr><td class="key">Phone:</td><td></td><td class="key">Date:</td><td></td></tr>
    <tr><td class="key">Re:</td><td></td><td class="key">CC:</td><td></td></tr>
  </table>
  <div class="checks"><span>Urgent</span><span>For Review</span><span>Please Comment</span><span>Please Reply</span><span>Please Recycle</span></div>
  <div class="emblem" role="img" aria-label="Faint brand emblem watermark"></div>
  <svg class="wave" style="height:70px"><use href="#swoosh" width="100%" height="100%"/></svg>
  <div class="footer">12 Birch Lane, Dover, DE 19901<br>555-0142 · loomtrellis.com</div>
</section>

<!-- letterhead -->
<div class="label" style="left:377px;top:192px;width:324px">Letterhead</div>
<section class="item sheet" style="left:377px;top:204px">
  <div class="brand"><span class="dot"></span>LoomTrellis</div>
  <div class="emblem" role="img" aria-label="Faint brand emblem watermark"></div>
  <svg class="wave" style="height:70px"><use href="#swoosh" width="100%" height="100%"/></svg>
  <div class="footer">12 Birch Lane, Dover, DE 19901<br>555-0142 · loomtrellis.com</div>
</section>

<!-- envelope front -->
<div class="label" style="left:732px;top:14px;width:444px">Envelope (Front)</div>
<section class="item envelope-front" style="left:732px;top:28px">
  <div class="brand"><span class="dot"></span>LoomTrellis</div>
  <div class="return">12 Birch Lane, Dover, DE 19901</div>
  <div class="emblem" role="img" aria-label="Faint brand emblem watermark"></div>
  <svg class="wave" style="height:44px"><use href="#swoosh" width="100%" height="100%"/></svg>
</section>

<!-- envelope backs -->
<div class="label" style="left:732px;top:268px;width:444px">Envelope (Back)</div>
<section class="item envelope-back" style="left:732px;top:282px">
  <svg class="flap" viewBox="0 0 444 100" preserveAspectRatio="none">
    <path d="M0 0 H444 L250 58 Q222 68 194 58Z" fill="url(#blueband)" stroke="#79bd2b" stroke-width="2"/>
  </svg>
  <div class="seal" style="top:30px"></div>
</section>
<div class="label" style="left:732px;top:392px;width:444px">Envelope (Back)</div>
<section class="item envelope-back" style="left:732px;top:406px">
  <svg class="flap" viewBox="0 0 444 100" preserveAspectRatio="none">
    <path d="M0 0 H444 L250 58 Q222 68 194 58Z" fill="#fff" stroke="#1f4f8e" stroke-width="1.5"/>
  </svg>
  <div class="seal" style="top:30px"></div>
</section>
<div class="label" style="left:732px;top:516px;width:444px">Envelope (Back)</div>
<section class="item envelope-back" style="left:732px;top:530px;height:94px">
  <svg class="flap" viewBox="0 0 444 94" preserveAspectRatio="none">
    <path d="M0 0 H444 L250 62 Q222 72 194 62Z" fill="#15171b"/>
  </svg>
  <div class="seal" style="top:26px"></div>
  <div class="seal-text" style="top:50px">loomtrellis.com</div>
</section>
</main>
</body>
</html>
```